Attract renters to our neighborhoods - inform renters who we are

Apartments in several neighborhoods. We want to attract renters who want to live along the lake or other near by neighborhoods. We want them to know that we have an apartment for them in their location.
The perfect location to spend your time.
When minutes matter LIVE where you work and play! (love this tag line)
Updates

www.kvtresidences.example Choose from over 3,700 apartments in Chicago’s most celebrated neighborhoods. 773-582-6041 Chicago’s most celebrated neighborhoods. 31 PROPERTIES

Target Market(s)

Sophisticated apartment renter who wants location, space, amenities

Industry/Entity Type

Apartment Rentals

Requirements
Must have
• Feel like I want to live there, or the ad is calling me
Nice to have
• Appeal to a sophisticated apartment renter. We have what you want, where you want to be.
Should not have
• Logo colors are black and red/burnt orange see attached logo

```html
<!DOCTYPE html>
<html lang="en">
<head>
<meta charset="utf-8">
<title>KVT Residences – When Minutes Matter</title>
<link href="https://fonts.googleapis.com/css2?family=Lato:wght@400;700;900&family=Oswald:wght@500&display=swap" rel="stylesheet">
<style>
  :root {
    --red: #c0141c;
    --dark: #2c3038;
    --ink: #1d1d1f;
    --white: #ffffff;
    --page-bg: #e9e9e9;
    --sky: #dfe8ef;
    --lake: #2f6f93;
    --city: #8a8d90;
  }
  * { box-sizing: border-box; margin: 0; padding: 0; }
  html, body { width: 1200px; height: 2963px; overflow: hidden; }
  body { background: var(--page-bg); font-family: 'Lato', sans-serif; position: relative; }

  .poster {
    position: absolute; left: 100px; top: 833px;
    width: 1000px; height: 1296px;
    background: var(--white);
    box-shadow: 0 6px 24px rgba(0,0,0,.18);
    overflow: hidden;
  }
  .poster > * { position: absolute; }

  .hero-photo {
    left: 0; top: 150px; width: 1000px; height: 349px;
    background: linear-gradient(180deg, var(--white) 0%, var(--sky) 22%, #9fc0d4 40%, var(--lake) 55%, #6f7a82 72%, var(--city) 100%);
  }

  .headline-top {
    left: 54px; top: 57px; width: 891px; height: 69px;
    background: var(--red); color: var(--white);
    font-size: 54px; font-weight: 400; line-height: 69px;
    text-align: center; letter-spacing: .5px;
  }
  .headline-top strong { font-weight: 900; margin-left: 14px; }
  .headline-bottom {
    left: 54px; top: 130px; width: 891px;
    color: var(--ink); font-size: 60px; font-weight: 400;
    line-height: 72px; letter-spacing: -.5px; text-align: center;
  }
  .headline-bottom strong { font-weight: 900; }

  .stat-bar { left: 0; top: 499px; width: 1000px; height: 128px; background: var(--dark); }
  .stat-box {
    left: 0; top: 499px; width: 245px; height: 128px; background: var(--red);
    color: var(--white); padding: 20px 0 0 54px;
  }
  .stat-number { font-family: 'Oswald', sans-serif; font-weight: 500; font-size: 64px; line-height: 68px; }
  .stat-label { font-weight: 900; font-size: 16px; letter-spacing: 1.5px; }
  .stat-copy {
    left: 265px; top: 530px; color: var(--white);
    font-size: 28px; line-height: 35px; font-weight: 700;
  }
  .chevrons { left: 880px; top: 499px; width: 120px; height: 110px; }

  .section-title {
    left: 0; top: 650px; width: 1000px; text-align: center;
    color: var(--red); font-size: 35px; font-weight: 900; letter-spacing: .5px;
  }

  .neighborhood-panel { left: 54px; top: 714px; width: 891px; height: 290px; background: var(--dark); }
  .neighborhood { top: 771px; width: 208px; }
  .neighborhood-photo { height: 170px; }
  .neighborhood-name {
    margin-top: 26px; color: var(--white); font-size: 14px; font-weight: 700;
  }
  .neighborhood-name::after {
    content: ""; display: block; width: 38px; height: 3px; margin-top: 6px; background: var(--red);
  }
  .n1 { left: 71px; }
  .n1 .neighborhood-photo { background: linear-gradient(180deg, #cdd9e3 0%, #7d8790 45%, #5f6b72 100%); }
  .n2 { left: 288px; }
  .n2 .neighborhood-photo { background: linear-gradient(180deg, #d7e2ea 0%, #3f7fa2 40%, #8a8e90 100%); }
  .n3 { left: 504px; }
  .n3 .neighborhood-photo { background: linear-gradient(180deg, #d5dfe6 0%, #7f9a7a 30%, #2a94a8 65%, #1d7f96 100%); }
  .n4 { left: 718px; }
  .n4 .neighborhood-photo { background: linear-gradient(180deg, #d3dde4 0%, #8d9792 35%, #2f8fa6 75%, #1f7488 100%); }

  .properties-box {
    left: 54px; top: 1030px; width: 191px; height: 137px; background: var(--red);
    color: var(--white); text-align: center; padding-top: 6px;
  }
  .properties-number { font-weight: 900; font-size: 84px; line-height: 88px; }
  .properties-label { font-size: 25px; font-weight: 400; }
  .tagline { left: 261px; top: 1038px; font-size: 36px; color: var(--ink); }
  .tagline em { font-style: normal; color: var(--red); }

  .cta-pill {
    left: 256px; top: 1096px; width: 689px; height: 61px; border-radius: 8px; overflow: hidden;
    display: flex; font-size: 24px; font-weight: 700; color: var(--white);
  }
  .cta-label { width: 341px; background: var(--dark); display: flex; align-items: center; justify-content: center; }
  .cta-url { flex: 1; background: var(--red); display: flex; align-items: center; justify-content: center; }

  .footer { left: 0; top: 1210px; width: 1000px; height: 86px; background: var(--dark); }
  .footer-phone-band { left: 649px; top: 1210px; width: 351px; height: 86px; background: var(--red); }
  .brand-box {
    left: 54px; top: 1210px; width: 158px; height: 86px; background: var(--white);
    display: flex; align-items: center; justify-content: center; gap: 8px;
    color: var(--ink); font-size: 46px; font-weight: 900; letter-spacing: 1px;
  }
  .brand-mark { width: 12px; height: 12px; background: var(--red); }
  .footer-text { left: 236px; top: 1210px; line-height: 86px; color: var(--white); font-size: 30px; font-weight: 700; }
  .phone-icon { left: 610px; top: 1234px; width: 38px; height: 38px; }
  .phone-number { left: 674px; top: 1210px; line-height: 86px; color: var(--white); font-size: 36px; font-weight: 900; }
</style>
</head>
<body>
  <div class="poster">
    <div class="hero-photo" role="img" aria-label="Aerial view of the Chicago skyline along the lakefront, with a hand holding a phone in the left foreground"></div>

    <div class="headline-top">WHEN MINUTES MATTER<strong>LIVE</strong></div>
    <div class="headline-bottom">WHERE YOU <strong>WORK AND PLAY!</strong></div>

    <div class="stat-bar"></div>
    <div class="stat-box">
      <div class="stat-number">3,700</div>
      <div class="stat-label">APARTMENTS</div>
    </div>
    <p class="stat-copy">Choose from over 3,700 apartments in<br>Chicago’s most celebrated neighborhoods.</p>
    <svg class="chevrons" viewBox="0 0 120 110" aria-hidden="true">
      <rect x="0" y="0" width="120" height="10" fill="#c0141c"/>
      <polygon points="15,24 120,24 110,37 25,37" fill="#c0141c"/>
      <polygon points="35,50 100,50 92,63 43,63" fill="#c0141c"/>
      <polygon points="57,76 78,76 67.5,88" fill="#c0141c"/>
    </svg>

    <h2 class="section-title">Explore Neighborhoods</h2>

    <div class="neighborhood-panel"></div>
    <div class="neighborhood n1">
      <div class="neighborhood-photo" role="img" aria-label="Aerial view of Gold Coast and Old Town towers"></div>
      <p class="neighborhood-name">Gold Coast &amp; Old Town</p>
    </div>
    <div class="neighborhood n2">
      <div class="neighborhood-photo" role="img" aria-label="Aerial view of River North high-rises by the lake"></div>
      <p class="neighborhood-name">River North</p>
    </div>
    <div class="neighborhood n3">
      <div class="neighborhood-photo" role="img" aria-label="Aerial view of the Lincoln Park beach and lakefront"></div>
      <p class="neighborhood-name">Lincoln Park</p>
    </div>
    <div class="neighborhood n4">
      <div class="neighborhood-photo" role="img" aria-label="Aerial view of the Lakeview harbor and neighborhood"></div>
      <p class="neighborhood-name">Lakeview</p>
    </div>

    <div class="properties-box">
      <div class="properties-number">31</div>
      <div class="properties-label">PROPERTIES</div>
    </div>
    <p class="tagline">Chicago’s <em>most celebrated neighborhoods.</em></p>
    <div class="cta-pill">
      <span class="cta-label">Find Your New Apartment!</span>
      <span class="cta-url">www.kvtresidences.example</span>
    </div>

    <div class="footer"></div>
    <div class="footer-phone-band"></div>
    <div class="brand-box"><span class="brand-mark"></span>KVT</div>
    <p class="footer-text">Schedule a Tour to call at</p>
    <svg class="phone-icon" viewBox="0 0 38 38" aria-hidden="true">
      <circle cx="19" cy="19" r="17" fill="#ffffff" stroke="#c0141c" stroke-width="2"/>
      <path d="M13 11c1-1 2-1 3 0l2 3c.5 1 0 2-1 2.5-.5.3-.5 1 0 2l2.5 3c.8.8 1.5.8 2 .2.6-.8 1.7-1.1 2.5-.5l2.6 2c.8.8.7 1.8-.2 2.7-2 2-5 1.6-8-1s-6-6.5-6.8-9.5c-.4-1.7.2-3.3 1.4-4.4z" fill="#c0141c"/>
    </svg>
    <p class="phone-number">773-582-6041</p>
  </div>
</body>
</html>
```